Need Business cards

Im a new realtor and already have a logo. I would like to purchase a Business card design that catches customer's attention, its creative, and modern.

Marisol Quintero
Realtor ®
(555) 318 4027
marisolqtrhomes@brindlemail.com

Target Market(s)

investors, buyers and seller, property management

Industry/Entity Type

real estate,

Contact Information for Business Card

Marisol Quintero

Requirements
Must have
• BOTH LOGOS, WOULD LIKE TO SEE WITH DIFFERENT OPTIONS WITH EITHER PICTURE

```html
<!DOCTYPE html>
<html lang="en">
<head>
<meta charset="utf-8">
<title>Marisol Quintero – Realtor Business Card</title>
<link href="https://fonts.googleapis.com/css2?family=Poppins:wght@400;500;600;700&display=swap" rel="stylesheet">
<style>
  :root {
    --backdrop: #5e4a35;
    --card: #ffffff;
    --gold: #d4a52a;
    --gold-deep: #b8871c;
    --gold-light: #f0c94a;
    --cream: #fdf4d2;
    --ink: #111111;
    --body: #222222;
    --brand-blue: #2e5aa8;
    --photo-top: #e9dccb;
    --photo-bottom: #8a6a4f;
  }
  * { margin: 0; padding: 0; box-sizing: border-box; }
  html, body { width: 900px; height: 1200px; overflow: hidden; }
  body {
    background: var(--backdrop);
    font-family: "Poppins", sans-serif;
    position: relative;
  }
  .card {
    position: absolute;
    left: 80px;
    width: 740px;
    height: 430px;
    background: var(--card);
    border-radius: 4px 40px 4px 40px;
    overflow: hidden;
  }
  .card--front { top: 135px; }
  .card--back {
    top: 643px;
    background: linear-gradient(180deg, var(--cream) 0%, #ffffff 22%, #ffffff 100%);
  }
  .wave { position: absolute; left: 0; top: 0; width: 740px; height: 430px; }

  .portrait {
    position: absolute;
    left: 28px; top: 25px;
    width: 250px; height: 390px;
    background: linear-gradient(180deg, var(--photo-top) 0%, var(--photo-bottom) 100%);
    border-radius: 120px 120px 6px 6px;
  }

  .monogram {
    position: absolute;
    display: flex; align-items: center; gap: 8px;
    color: var(--gold);
    font-weight: 600;
    line-height: 1;
  }
  .monogram__square { background: var(--gold); }
  .card--front .monogram { left: 340px; top: 62px; font-size: 54px; }
  .card--front .monogram__square { width: 14px; height: 14px; }

  .identity { position: absolute; left: 337px; top: 176px; }
  .identity__name { font-size: 24px; font-weight: 600; color: var(--ink); letter-spacing: 0.5px; }
  .identity__title { font-size: 16px; font-weight: 500; color: var(--gold); letter-spacing: 0.5px; margin-top: 2px; }

  .contact { position: absolute; left: 338px; top: 246px; list-style: none; }
  .contact__item {
    display: flex; align-items: center; gap: 10px;
    font-size: 17px; color: var(--body); height: 29px;
  }
  .contact__icon { width: 17px; height: 17px; flex: none; }

  .brokerage {
    position: absolute; left: 338px; top: 323px;
    color: var(--brand-blue);
    font-size: 24px; font-weight: 600; line-height: 1;
    letter-spacing: 0.5px;
  }

  .card--back .monogram {
    left: 0; right: 0; top: 140px; justify-content: center;
    font-size: 80px;
  }
  .card--back .monogram__square { width: 20px; height: 20px; }
  .signature { position: absolute; left: 0; right: 0; top: 286px; text-align: center; color: var(--gold); }
  .signature__name { font-size: 24px; font-weight: 600; letter-spacing: 0.5px; }
  .signature__title {
    display: flex; align-items: center; justify-content: center; gap: 10px;
    font-size: 15px; font-weight: 500; letter-spacing: 1px; margin-top: 0;
  }
  .signature__rule { width: 70px; height: 1px; background: var(--gold); }

  .homestead {
    position: absolute; left: 62px; top: 330px;
    width: 90px; height: 32px;
    background: var(--gold);
    border-radius: 4px 4px 0 0;
  }
</style>
</head>
<body>

<section class="card card--front">
  <svg class="wave" viewBox="0 0 740 430" aria-hidden="true">
    <defs>
      <linearGradient id="goldFront" x1="0" y1="0" x2="1" y2="0">
        <stop offset="0" stop-color="#c99a24"/>
        <stop offset="0.6" stop-color="#d8ab30"/>
        <stop offset="1" stop-color="#f0c94a"/>
      </linearGradient>
    </defs>
    <path d="M0 330 C150 300 300 350 450 340 C580 330 680 300 740 305 L740 430 L0 430 Z" fill="#f4e2a8"/>
    <path d="M0 345 C150 330 280 380 450 368 C590 356 680 330 740 322 L740 430 L0 430 Z" fill="url(#goldFront)"/>
  </svg>

  <div class="portrait" role="img" aria-label="Portrait photograph of the realtor"></div>

  <div class="monogram"><span>MQ</span><span class="monogram__square"></span></div>

  <div class="identity">
    <h1 class="identity__name">MARISOL QUINTERO</h1>
    <p class="identity__title">REALTOR ®</p>
  </div>

  <ul class="contact">
    <li class="contact__item">
      <svg class="contact__icon" viewBox="0 0 24 24" aria-hidden="true"><path fill="#d4a52a" d="M6.6 10.8a15.1 15.1 0 0 0 6.6 6.6l2.2-2.2a1 1 0 0 1 1-.25 11.4 11.4 0 0 0 3.6.57 1 1 0 0 1 1 1V20a1 1 0 0 1-1 1A17 17 0 0 1 3 4a1 1 0 0 1 1-1h3.5a1 1 0 0 1 1 1c0 1.25.2 2.45.57 3.57a1 1 0 0 1-.25 1z"/></svg>
      <span>(555) 318 4027</span>
    </li>
    <li class="contact__item">
      <svg class="contact__icon" viewBox="0 0 24 24" aria-hidden="true"><rect x="2" y="5" width="20" height="14" rx="1" fill="#d4a52a"/><path d="M2.5 5.5 12 13l9.5-7.5" fill="none" stroke="#fff" stroke-width="1.6"/></svg>
      <span>marisolqtrhomes@brindlemail.com</span>
    </li>
  </ul>

  <p class="brokerage">KEYSTRIDE REALTY</p>
</section>

<section class="card card--back">
  <svg class="wave" viewBox="0 0 740 430" aria-hidden="true">
    <defs>
      <linearGradient id="goldBack" x1="0" y1="0" x2="1" y2="0">
        <stop offset="0" stop-color="#c99a24"/>
        <stop offset="0.6" stop-color="#d8ab30"/>
        <stop offset="1" stop-color="#f0c94a"/>
      </linearGradient>
    </defs>
    <path d="M0 322 C150 310 300 360 460 360 C600 360 690 330 740 320 L740 430 L0 430 Z" fill="#fbeec0"/>
    <path d="M0 362 C180 350 330 385 480 385 C610 385 690 370 740 362 L740 430 L0 430 Z" fill="url(#goldBack)"/>
  </svg>

  <div class="homestead" role="img" aria-label="Small silhouette of a house and tree on a hill"></div>

  <div class="monogram"><span>MQ</span><span class="monogram__square"></span></div>

  <div class="signature">
    <p class="signature__name">MARISOL QUINTERO</p>
    <p class="signature__title"><span class="signature__rule"></span>REALTOR<span class="signature__rule"></span></p>
  </div>
</section>

</body>
</html>
```